Wedding Vows Poster for a Frame (anniversary gift )

I need an 8 X11 copy of both or wedding vows that I can frame in a classy and timeless modern font to frame for our house .

see file attach for text (vows)

project is now close thank you for all your help

Wedding

```html
<!DOCTYPE html>
<html lang="en">
<head>
<meta charset="utf-8">
<title>Wedding Vows Poster – Marcus &amp; Elena</title>
<link href="https://fonts.googleapis.com/css2?family=Cinzel:wght@400;500&display=swap" rel="stylesheet">
<style>
  :root {
    --backdrop: #eeeeee;
    --paper: #ffffff;
    --ink: #161616;
    --flourish: #bcbcbc;
    --flourish-soft: #d9d9d9;
    --ornament: #2a2a2a;
  }
  html, body {
    margin: 0;
    width: 1200px;
    height: 822px;
    overflow: hidden;
    background: var(--backdrop);
  }
  .poster {
    position: absolute;
    left: 318px;
    top: 11px;
    width: 563px;
    height: 800px;
    background: var(--paper);
    box-shadow: 4px 6px 10px rgba(0,0,0,0.35);
    font-family: "Cinzel", serif;
    color: var(--ink);
    overflow: hidden;
  }
  .flourish {
    position: absolute;
    border-radius: 40% 60% 55% 45%;
    background: radial-gradient(ellipse at 50% 50%, var(--flourish) 0%, var(--flourish-soft) 60%, var(--paper) 100%);
  }
  .flourish--upper-right { left: 305px; top: 25px; width: 210px; height: 410px; }
  .flourish--lower-left { left: 25px; top: 420px; width: 185px; height: 360px; }
  .crest {
    position: absolute;
    width: 72px;
    height: 22px;
    background: linear-gradient(180deg, var(--ornament), #5a5a5a);
    border-radius: 50% 50% 8px 8px;
  }
  .crest--his { left: 50px; top: 18px; }
  .crest--hers { left: 250px; top: 435px; }
  .vow-title {
    position: absolute;
    margin: 0;
    font-weight: 400;
    font-size: 20px;
    line-height: 1;
    white-space: nowrap;
  }
  .vow-title .initial { font-size: 84px; line-height: 1; }
  .vow-title--his { left: 52px; top: 46px; }
  .vow-title--hers { left: 252px; top: 462px; }
  .vow {
    position: absolute;
    display: flex;
    flex-direction: column;
    align-items: center;
    text-align: center;
  }
  .vow--his { left: 22px; top: 160px; width: 316px; }
  .vow--hers { left: 238px; top: 572px; width: 300px; }
  .vow-text { margin: 0; }
  .vow--his .vow-text { font-size: 9.8px; line-height: 10.9px; }
  .vow--hers .vow-text { font-size: 10.6px; line-height: 12.3px; }
  .vow-text .gap { display: block; height: 9px; }
  .signature { margin: 0; }
  .vow--his .signature { margin-top: 9px; font-size: 9px; }
  .vow--hers .signature { margin-top: 11px; font-size: 10px; line-height: 13px; }
  .signature .mark {
    display: block;
    margin: 2px auto 0;
    width: 20px;
    height: 7px;
    background: var(--ornament);
    border-radius: 50%;
  }
</style>
</head>
<body>
  <main class="poster">
    <div class="flourish flourish--upper-right" role="img" aria-label="Grey swirling floral flourish"></div>
    <div class="flourish flourish--lower-left" role="img" aria-label="Grey swirling floral flourish"></div>

    <div class="crest crest--his" role="img" aria-label="Small black floral crown ornament"></div>
    <h1 class="vow-title vow-title--his"><span class="initial">M</span>arcus to Elena</h1>
    <section class="vow vow--his">
      <p class="vow-text">
        Three years ago I fell in love with you on our<br>
        journey trough Peru,<br>
        your love for life , your drive, your beautiful<br>
        smile, and natural beauty were at the time<br>
        what got my attention.<br>
        Now that I know much more about you I have<br>
        realize how much more complete of an<br>
        individual you are.<br>
        For a long time I wish I had meet you before<br>
        however only now I can appreciate you fully.<br>
        I love you Elena<br>
        “This ring represents my commitment to you<br>
        as your partner and to our marriage.<br>
        As your partner I am committed to a life<br>
        where we can have it all.&nbsp; By all I mean an<br>
        amazing relationship where we can share a<br>
        fulfilling life together.<br>
        As your husband I promise to be loyal and give<br>
        you the best that I can, protect and cherish<br>
        you I will always be there for you trough<br>
        good and hard time.<br>
        <span class="gap"></span>
        I will grow old with you and love you<br>
        forever.
      </p>
      <p class="signature">Marcus</p>
    </section>

    <div class="crest crest--hers" role="img" aria-label="Small black floral crown ornament"></div>
    <h2 class="vow-title vow-title--hers"><span class="initial">E</span>lena to Marcus</h2>
    <section class="vow vow--hers">
      <p class="vow-text">
        “This ring represents my commitment to<br>
        you as your partner and to our marriage.<br>
        As your partner I promise to always do my<br>
        best to support, respect, be compassionate<br>
        and loving to you.&nbsp; And as your wife, I<br>
        promise to always to my best to be honest,<br>
        trust worthy trust and during<br>
        challenging times to have the faith that<br>
        we will somehow overcome it and be even<br>
        stronger on the other side.<br>
        <span class="gap"></span>
        Marc, you are my favorite person, I love<br>
        you with all my heart and I am so very<br>
        proud to be your wife. ”
      </p>
      <p class="signature">Love always,<br>E<span class="mark" role="img" aria-label="Tiny flourish ornament"></span></p>
    </section>
  </main>
</body>
</html>
```